Brookmere Osteopathy flyer

I want a clean clear DL flyer (but also want an A4 poster) promoting a new Osteopathic business in a semi rural area in Tasmania (Australia).
It can have pictures like the examples attached to show people what Osteopathy is (its like Chiropractic and physiotherapy).
I am the sole practioner and am male, so any pictures would be best to be a white male if possible.
I've attached some wording, you can use all, or none of it
I don't have a phone number for the business yet
info@brookmereosteopathy.example
www.brookmereosteopathy.example
Target Market(s)
Australians, from tradies, professionals, babies to retired people
Industry/Entity Type
Health
Look and feel

```html
<!DOCTYPE html>
<html lang="en">
<head>
<meta charset="utf-8">
<title>Brookmere Osteopathy – DL Flyer</title>
<link rel="stylesheet" href="https://fonts.googleapis.com/css2?family=Questrial&display=swap">
<style>
  :root {
    --backdrop: #e4e4e4;
    --brand-blue: #0f96d0;
    --brand-orange: #f7943a;
    --sun-yellow: #ffb400;
    --deep-orange: #ff8a00;
    --text-grey: #4a4a4a;
    --white: #ffffff;
  }
  * { box-sizing: border-box; margin: 0; padding: 0; }
  html, body { width: 1200px; height: 1143px; overflow: hidden; background: var(--backdrop); }
  body { position: relative; font-family: "Questrial", sans-serif; }

  .flyer { position: absolute; top: 189px; width: 366px; height: 732px; overflow: hidden; }
  .flyer--front { left: 203px; background: var(--brand-blue); }
  .flyer--back { left: 639px; background: var(--white); }

  .flyer__art { position: absolute; inset: 0; }

  .frame { position: absolute; border: 2px solid; pointer-events: none; }
  .frame--outer { left: 18px; top: 17px; width: 330px; height: 700px; }
  .frame--inner { left: 26px; top: 25px; width: 314px; height: 684px; }
  .flyer--front .frame { border-color: var(--brand-orange); }
  .flyer--back .frame { border-color: var(--brand-blue); }

  /* front */
  .front-brand { position: absolute; left: 78px; top: 398px; width: 210px; height: 210px;
    border-radius: 50%; border: 3px solid var(--white); display: flex; flex-direction: column;
    align-items: center; justify-content: center; text-align: center; color: var(--white); }
  .front-brand__name { font-size: 26px; line-height: 1.15; }
  .front-phone { position: absolute; left: 0; width: 100%; top: 630px; text-align: center;
    color: var(--white); font-size: 36px; letter-spacing: 0.3px; }
  .front-web { position: absolute; left: 0; width: 100%; top: 681px; text-align: center;
    color: var(--white); font-size: 13px; letter-spacing: 0.6px; text-transform: uppercase; }

  /* back */
  .reasons { position: absolute; left: 51px; top: 42px; color: var(--white); }
  .reasons__title { font-size: 21px; line-height: 19px; font-weight: 400; text-transform: uppercase; letter-spacing: -0.2px; }
  .reasons__list { list-style: none; margin-top: 12px; }
  .reasons__list li { position: relative; padding-left: 22px; font-size: 13.5px; line-height: 21.1px; }
  .reasons__list li::before { content: ""; position: absolute; left: 5px; top: 9px; width: 4px; height: 4px; border-radius: 50%; background: var(--white); }

  .photo-round { position: absolute; border-radius: 50%; }
  .photo-round--baby { left: 28px; top: 326px; width: 150px; height: 150px; background: radial-gradient(circle at 50% 45%, #e9c7b0, #8fa6c8 60%, #3f8fc4); }
  .photo-round--neck { left: 182px; top: 322px; width: 148px; height: 148px; background: radial-gradient(circle at 45% 50%, #e4b89c, #c7d2e2 55%, #2a2f3a 85%); }

  .about { position: absolute; left: 43px; top: 505px; width: 285px; font-size: 13px; line-height: 17px;
    color: var(--text-grey); text-align: justify; hyphens: auto; }

  .contact-brand { position: absolute; left: 36px; top: 605px; width: 94px; height: 94px; border-radius: 50%;
    border: 2px solid var(--brand-blue); display: flex; align-items: center; justify-content: center;
    text-align: center; color: var(--brand-blue); font-size: 12.5px; line-height: 1.2; }
  .contact { position: absolute; left: 140px; top: 612px; }
  .contact__phone { display: flex; align-items: center; gap: 6px; color: var(--brand-blue); font-size: 21px; }
  .contact__phone svg { flex: none; }
  .contact__line { color: var(--text-grey); font-size: 11px; line-height: 17px; margin-left: 1px; }
  .contact__line--first { margin-top: 3px; }
  .contact__web { position: absolute; left: 132px; top: 674px; width: 198px; height: 16px; border-radius: 8px;
    background: var(--brand-blue); color: var(--white); font-size: 9px; line-height: 16px; text-align: center;
    text-transform: uppercase; letter-spacing: 0.3px; }
</style>
</head>
<body>

<section class="flyer flyer--front">
  <svg class="flyer__art" width="366" height="732" viewBox="0 0 366 732">
    <defs>
      <linearGradient id="backTone" x1="0" y1="0" x2="1" y2="1">
        <stop offset="0" stop-color="#d9d3cf"/>
        <stop offset="0.35" stop-color="#8a6a58"/>
        <stop offset="0.75" stop-color="#b5856a"/>
        <stop offset="1" stop-color="#9c6d52"/>
      </linearGradient>
    </defs>
    <path role="img" aria-label="Photo: practitioner's hands treating a patient's upper back"
      d="M0 0 H366 V413 Q183 500 0 413 Z" fill="url(#backTone)"/>
  </svg>
  <div class="frame frame--outer"></div>
  <div class="frame frame--inner"></div>
  <div class="front-brand"><p class="front-brand__name">Brookmere<br>Osteopathy</p></div>
  <p class="front-phone">(555) 0142-7788</p>
  <p class="front-web">www.brookmereosteopathy.example</p>
</section>

<section class="flyer flyer--back">
  <svg class="flyer__art" width="366" height="732" viewBox="0 0 366 732">
    <defs>
      <linearGradient id="sunTone" x1="0" y1="0" x2="0" y2="1">
        <stop offset="0" stop-color="#ffb000"/>
        <stop offset="0.5" stop-color="#ff9a10"/>
        <stop offset="1" stop-color="#ffbe00"/>
      </linearGradient>
    </defs>
    <rect role="img" aria-label="Photo, tinted orange: woman relaxing during a head and neck treatment"
      x="0" y="0" width="366" height="420" fill="url(#sunTone)"/>
    <path d="M0 410 Q183 330 366 404 V732 H0 Z" fill="#ffffff"/>
  </svg>
  <div class="frame frame--outer"></div>
  <div class="frame frame--inner"></div>

  <div class="reasons">
    <h2 class="reasons__title">Common reasons people<br>visit an osteopath:</h2>
    <ul class="reasons__list">
      <li>Back / neck pain</li>
      <li>Headaches / migraines</li>
      <li>Joint and muscle pain</li>
      <li>Pregnancy-related discomfort</li>
      <li>Disc related issues</li>
      <li>Sciatica</li>
      <li>Plantar fasciitis</li>
      <li>Tendonitis / Bursitis</li>
      <li>Adhesive capsulitis (frozen shoulder)</li>
      <li>Tennis / Golfers elbow</li>
    </ul>
  </div>

  <div class="photo-round photo-round--baby" role="img" aria-label="Photo: gentle cranial treatment for a sleeping baby"></div>
  <div class="photo-round photo-round--neck" role="img" aria-label="Photo: practitioner treating a woman's neck on a table"></div>

  <p class="about">Osteopaths use a combination of joint manipulation, targeted deep tissue massage and stretching to improve function, relieve pain and support the body’s ability to heal itself.</p>

  <div class="contact-brand">Brookmere<br>Osteopathy</div>
  <div class="contact">
    <p class="contact__phone">
      <svg width="21" height="21" viewBox="0 0 24 24" aria-hidden="true">
        <circle cx="12" cy="12" r="12" fill="#f7943a"/>
        <path d="M8.2 6.2c.4-.3 1-.3 1.3.1l1.4 1.9c.3.4.2 1-.1 1.3l-.8.7c.6 1.4 1.7 2.6 3.1 3.3l.8-.8c.4-.3.9-.4 1.3-.1l1.9 1.4c.4.3.4.9.1 1.3l-1 1.1c-.6.6-1.5.8-2.3.5-3.1-1.2-5.5-3.7-6.7-6.8-.3-.8-.1-1.7.5-2.3z" fill="#ffffff"/>
      </svg>
      (555) 0142-7788
    </p>
    <p class="contact__line contact__line--first">info@brookmereosteopathy.example</p>
    <p class="contact__line">24 Wattle Creek road, Brookmere</p>
  </div>
  <p class="contact__web">www.brookmereosteopathy.example</p>
</section>

</body>
</html>
```